New, clean letterhead for law firm in Colorado using recently designed logo.

Professional letterhead for established law firm rebranding. We service high end clientele with mostly family law and personal injury cases. Need source files for future changes. Prefer logo at top, names of members and staff in left margin, contact info in footer.

Target Market(s)

High wealth individuals

Contact Information for Business Card

Need options for traditional and square two sided business cards

Font styles to use
Serif

Colors
0555a3

Requirements
Must have
• Our logo; blue, gray, and white; modern feel.
Should not have
• Images of people

```html
<!DOCTYPE html>
<html lang="en">
<head>
<meta charset="utf-8">
<title>Hartwell Ashford Law – Business Card</title>
<link rel="stylesheet" href="https://fonts.googleapis.com/css2?family=Arimo:wght@400;700&display=swap">
<style>
  :root {
    --backdrop: #1f1f1f;
    --card: #fbfafc;
    --brand-blue: #2b6cb4;
    --text-gray: #5a5a5a;
    --rule-gray: #9a9a9a;
  }
  * { box-sizing: border-box; margin: 0; padding: 0; }
  html, body {
    width: 1200px; height: 900px; overflow: hidden;
    background: var(--backdrop);
    font-family: "Arimo", Arial, sans-serif;
  }
  .canvas {
    width: 1200px; height: 900px;
    display: flex; flex-direction: column; align-items: center; justify-content: center;
    gap: 36px;
  }
  .card {
    position: relative;
    width: 700px; height: 400px;
    background: var(--card);
    box-shadow: 0 10px 30px rgba(0,0,0,.45);
    overflow: hidden;
  }
  .card::after {
    content: ""; position: absolute; left: 0; right: 0; bottom: 0;
    height: 10px; background: var(--brand-blue);
  }
  /* front */
  .card--front { display: flex; align-items: center; justify-content: center; }
  .firm-name {
    font-family: "Arimo", Arial, sans-serif;
    font-weight: 700; font-size: 34px; letter-spacing: 3px;
    color: var(--brand-blue); text-transform: uppercase;
    margin-bottom: 10px;
  }
  /* back */
  .identity {
    position: absolute; top: 150px; left: 0; width: 100%;
    display: flex; justify-content: center; align-items: stretch; gap: 20px;
    padding-right: 40px;
  }
  .person { text-align: right; padding-top: 2px; }
  .person__name { font-weight: 700; font-size: 27px; color: var(--brand-blue); line-height: 1; }
  .person__title { font-size: 18px; color: var(--text-gray); margin-top: 2px; }
  .divider { width: 1.5px; background: var(--brand-blue); height: 62px; }
  .contacts { list-style: none; font-size: 15.5px; color: var(--text-gray); line-height: 1.45; }
  .contacts li { display: flex; align-items: center; gap: 12px; }
  .contacts svg { width: 16px; height: 16px; flex: none; }
  .address {
    position: absolute; left: 0; width: 100%; bottom: 44px;
    text-align: center; font-size: 17px; color: var(--text-gray);
  }
</style>
</head>
<body>
<main class="canvas">
  <section class="card card--front">
    <h1 class="firm-name">Hartwell Ashford Law, LLC</h1>
  </section>

  <section class="card card--back">
    <div class="identity">
      <div class="person">
        <p class="person__name">Daniel Moore</p>
        <p class="person__title">President</p>
      </div>
      <div class="divider"></div>
      <ul class="contacts">
        <li>
          <svg viewBox="0 0 16 16" aria-hidden="true"><path d="M3 1.5l2.5 0 1 3.2-1.6 1.2a8 8 0 0 0 5.2 5.2l1.2-1.6 3.2 1V13c0 .8-.7 1.5-1.5 1.5A11.5 11.5 0 0 1 1.5 3C1.5 2.2 2.2 1.5 3 1.5z" fill="var(--brand-blue)"/></svg>
          +00 000 000 000
        </li>
        <li>
          <svg viewBox="0 0 16 16" aria-hidden="true"><rect x="1.5" y="3.5" width="13" height="9" fill="none" stroke="var(--brand-blue)" stroke-width="1.2"/><path d="M1.5 3.5l6.5 5 6.5-5M1.5 12.5l5-4.2M14.5 12.5l-5-4.2" fill="none" stroke="var(--brand-blue)" stroke-width="1.2"/></svg>
          info@hartwellashford.com
        </li>
        <li>
          <svg viewBox="0 0 16 16" aria-hidden="true"><g fill="none" stroke="var(--brand-blue)" stroke-width="1.1"><circle cx="8" cy="8" r="6.5"/><ellipse cx="8" cy="8" rx="3" ry="6.5"/><path d="M1.5 8h13M2.5 4.8h11M2.5 11.2h11"/></g></svg>
          www.hartwellashford.com
        </li>
      </ul>
    </div>
    <p class="address">0000 Street Ave. unit 000 New York, CA 00000</p>
  </section>
</main>
</body>
</html>
```